Moms Beyond Gnatflies

My company name is Moms beyond gnatflies. We do residential and commercial mosquito control. See attached brochure and logo.

Target Market(s)

My target market is upper middle class families in the midwestern part of the US.

Requirements
Must have
• Form to collect customer information

```html
<!DOCTYPE html>
<html lang="en">
<head>
<meta charset="utf-8">
<title>Moms Beyond Gnatflies – Mosquito Control</title>
<link rel="stylesheet" href="https://fonts.googleapis.com/css2?family=Arimo:wght@400;700&family=Montserrat:wght@600;800&family=Nunito:wght@900&family=Yanone+Kaffeesatz:wght@400;600;700&display=swap">
<style>
:root{
  --green-dark:#0b5e2c;
  --green-deep:#0a4a12;
  --green-bright:#1fb50f;
  --nav-top:#2fb61a;
  --nav-bottom:#0d7a0c;
  --nav-active:#0b350a;
  --yellow:#fff200;
  --yellow-soft:#ffee3a;
  --ink:#222;
  --grey:#555;
  --grey-light:#777;
  --white:#fff;
}
*{box-sizing:border-box;margin:0;padding:0}
html,body{width:1200px;height:1100px;overflow:hidden;background:var(--white)}
body{position:relative;font-family:"Arimo",Arial,sans-serif;color:var(--ink)}
.abs{position:absolute}

/* header */
.brand{left:160px;top:18px;display:flex;align-items:flex-start;gap:10px}
.brand-mark{width:22px;height:22px;background:var(--yellow);margin-top:8px}
.brand-name{font-family:"Yanone Kaffeesatz",sans-serif;font-weight:700;color:var(--green-dark);font-size:36px;line-height:36px}
.tagline{left:516px;top:12px;width:560px;font-family:"Nunito",sans-serif;font-weight:900;font-size:29px;line-height:30px;color:var(--green-dark)}
.callout{left:553px;top:88px;font-family:"Yanone Kaffeesatz",sans-serif;font-weight:700;font-size:50px;line-height:56px;color:#333;white-space:nowrap}
.callout .area{color:var(--green-bright)}
.callout .num{color:var(--green-dark)}
.callout .note{font-size:25px;font-weight:400;color:var(--grey-light);margin-left:8px}

/* navigation */
.nav{left:0;top:155px;width:1200px;height:38px;background:linear-gradient(var(--nav-top),var(--nav-bottom))}
.nav ul{list-style:none;display:flex;margin-left:140px;height:38px}
.nav li{font-family:"Montserrat",sans-serif;font-weight:600;font-size:13px;color:var(--white);display:flex;align-items:center;justify-content:center;border-right:1px solid rgba(255,255,255,.35)}
.nav li.active{background:var(--nav-active)}

/* sky background */
.sky{left:0;top:193px;width:1200px;height:785px;background:
  radial-gradient(ellipse 400px 160px at 120px 300px,rgba(255,255,255,.8),transparent),
  radial-gradient(ellipse 500px 200px at 700px 700px,rgba(255,255,255,.85),transparent),
  linear-gradient(#d9ebf7 0%,#a9d0ec 25%,#cfe4f3 55%,#ffffff 100%)}

/* info sections */
.qa{left:142px;width:540px}
.qa h2{display:flex;align-items:flex-end;white-space:nowrap;height:32px}
.qa h2 svg{flex-shrink:0;margin-bottom:2px}
.qa .key{font-family:"Montserrat",sans-serif;font-weight:800;font-size:33px;line-height:30px;color:var(--green-dark);margin-left:4px;margin-right:4px}
.qa .rest{font-family:"Yanone Kaffeesatz",sans-serif;font-weight:600;font-size:26px;line-height:24px;color:#333;text-transform:uppercase}
.qa p{margin-top:8px;font-size:14px;line-height:20px;color:var(--grey)}

.eco-heading{right:142px;top:206px;z-index:2;text-align:right;font-family:"Yanone Kaffeesatz",sans-serif;font-weight:400;font-size:31px;line-height:32px;color:var(--grey-light)}
.eco-heading b{font-weight:700;color:var(--green-dark)}
.photo{background:linear-gradient(135deg,#6f8f52,#c9b494)}

.banner-text{left:148px;top:650px;font-family:"Yanone Kaffeesatz",sans-serif;font-weight:600;font-size:23px;line-height:28px;color:var(--green-dark);white-space:nowrap}
.bee-text{left:140px;top:716px;width:200px;transform:rotate(-12deg);text-align:center;font-family:"Yanone Kaffeesatz",sans-serif;font-weight:700;font-size:24px;line-height:22px;color:#111}
.bee-text .big{display:block;font-size:33px;line-height:30px}
.pitch{left:373px;top:694px;width:320px;font-size:17px;line-height:22px;color:#111}
.pitch strong{display:block;margin-top:24px;line-height:24px}

/* request form */
.form-title{left:754px;top:592px;z-index:2;font-family:"Yanone Kaffeesatz",sans-serif;font-weight:700;font-size:25px;line-height:26px;color:var(--green-dark)}
.form-panel{left:753px;top:613px;width:330px;height:337px;background:var(--green-deep);border-radius:0 14px 0 14px}
.field{position:absolute;left:0;display:flex;align-items:center;width:330px}
.field label{width:63px;text-align:right;font-size:14px;color:var(--white)}
.field span{margin-left:8px;width:243px;height:27px;background:var(--white);border:1px solid #b9c7b6}
.question{position:absolute;left:15px;top:206px;font-size:14px;color:#e5efe2}
.choice{position:absolute;top:234px;display:flex;align-items:center;gap:8px;font-size:14px;color:var(--white)}
.choice i{width:14px;height:14px;background:#ddd;display:block}
.submit{position:absolute;left:188px;top:250px;width:128px;height:49px;border-radius:4px;background:linear-gradient(#fff37a,#e2c11b);display:flex;align-items:center;justify-content:center;font-family:"Montserrat",sans-serif;font-weight:800;font-size:19px;color:var(--green-dark)}

.footer-shade{left:120px;top:975px;width:1000px;height:16px;background:radial-gradient(ellipse at top,rgba(0,0,0,.12),transparent 70%)}
.copyright{left:0;top:998px;width:1283px;text-align:center;font-size:12px;color:var(--green-dark)}
</style>
</head>
<body>

<header>
  <div class="abs brand">
    <span class="brand-mark"></span>
    <div class="brand-name">Moms<br>Beyond<br>Gnatflies</div>
  </div>
  <svg class="abs" style="left:510px;top:8px" width="565" height="70" viewBox="0 0 565 70"><polygon points="2,0 560,20 555,30 40,66 8,58" fill="var(--yellow)"/></svg>
  <p class="abs tagline">Rid your outside areas of pesky and dangerous bugs the safe way!</p>
  <p class="abs callout">CALL <span class="area">(630)</span> <span class="num">555-0147</span><span class="note">to schedule an evaluation.</span></p>
</header>

<nav class="abs nav">
  <ul>
    <li class="active" style="width:114px">HOME</li>
    <li style="width:126px">ABOUT</li>
    <li style="width:147px">PRODUCTS</li>
    <li style="width:135px">SERVICES</li>
    <li style="width:138px">CONTACT</li>
  </ul>
</nav>

<div class="abs sky" role="img" aria-label="Blue sky with soft white clouds"></div>

<main>
  <section class="abs qa" style="top:240px">
    <h2><svg width="58" height="24" viewBox="0 0 58 26"><polygon points="0,8 14,8 14,0 44,0 44,8 58,8 29,26" fill="var(--green-deep)"/></svg><span class="key">WHAT</span><span class="rest">is Moms Beyond Gnatflies?</span></h2>
    <p style="width:420px">Moms Beyond Gnatflies is the only scheduled spraying service devoted exclusively to protecting your outdoor area against mosquitoes and other pests all season long!</p>
  </section>
  <section class="abs qa" style="top:371px">
    <h2><svg width="58" height="24" viewBox="0 0 58 26"><polygon points="0,8 14,8 14,0 44,0 44,8 58,8 29,26" fill="var(--green-deep)"/></svg><span class="key">WHY</span><span class="rest">use Moms Beyond Gnatflies?</span></h2>
    <p style="margin-top:20px">West Nile Virus is a real threat! Illinois is one of the states with the most confirmed human cases.&nbsp; M.B.G! will protect your business against West Nile and eliminate or reduce the dangers of Encephalitis and allergic reactions caused by insect bites.</p>
  </section>
  <section class="abs qa" style="top:509px">
    <h2><svg width="58" height="24" viewBox="0 0 58 26"><polygon points="0,8 14,8 14,0 44,0 44,8 58,8 29,26" fill="var(--green-deep)"/></svg><span class="key">WHERE</span><span class="rest">can I spray Moms Beyond Gnatflies?</span></h2>
    <p style="width:520px">Anywhere outside. M.B.G! offers excellent service for public pools, outdoor cafés and beer gardens, baseball fields, courtyards, public places such as fountains or town squares, and office gathering areas.</p>
  </section>

  <svg class="abs" style="left:137px;top:642px" width="560" height="38" viewBox="0 0 560 38"><polygon points="0,0 558,22 556,30 4,36" fill="var(--yellow)"/></svg>
  <p class="abs banner-text">Once applied, M.B.G! is a long acting product that remains effective for weeks.</p>

  <svg class="abs" style="left:142px;top:704px" width="196" height="162" viewBox="0 0 196 162"><ellipse cx="98" cy="81" rx="96" ry="79" fill="var(--yellow-soft)"/></svg>
  <p class="abs bee-text">Now offering<br>“BEE FRIENDLY”<br>bee deterrent!<span class="big">great for outside<br>eating areas!</span></p>

  <div class="abs pitch">
    Keep your customers and employees enjoying the summer weather without the inconvenience of mosquitoes, ticks, lice and other insects.
    <strong>Call (630) 555-0147 to schedule an evaluation appointment or feel out the form to the right.</strong>
  </div>

  <div class="abs photo" style="left:735px;top:281px;width:103px;height:164px" role="img" aria-label="Parent and child walking on a garden path"></div>
  <div class="abs photo" style="left:844px;top:281px;width:220px;height:92px;background:linear-gradient(135deg,#c8743a,#e9c9a4)" role="img" aria-label="Friends sharing drinks at an outdoor café"></div>
  <div class="abs photo" style="left:735px;top:448px;width:214px;height:129px;background:linear-gradient(#3c3a2a,#2f7fa8)" role="img" aria-label="Hotel swimming pool with parasols at dusk"></div>
  <div class="abs photo" style="left:953px;top:377px;width:111px;height:200px;background:linear-gradient(135deg,#9a2f35,#6f7d5c)" role="img" aria-label="Business people chatting in a courtyard"></div>
  <svg class="abs" style="left:668px;top:210px" width="142" height="142" viewBox="0 0 142 142"><circle cx="71" cy="71" r="66" fill="rgba(255,255,255,.92)" stroke="var(--green-dark)" stroke-width="5"/><circle cx="71" cy="71" r="52" fill="none" stroke="var(--green-dark)" stroke-width="2"/></svg>
  <p class="abs eco-heading">environmentally-friendly<br><b>EPA-APPROVED</b> treatment</p>

  <svg class="abs" style="left:730px;top:588px" width="360" height="365" viewBox="0 0 360 365"><polygon points="2,0 358,18 354,362 24,362" fill="var(--yellow)"/></svg>
  <form class="abs form-panel" aria-label="Request information">
    <div class="field" style="top:22px"><label>Name</label><span></span></div>
    <div class="field" style="top:67px"><label>Email</label><span></span></div>
    <div class="field" style="top:113px"><label>Phone</label><span></span></div>
    <div class="field" style="top:155px"><label>Address</label><span></span></div>
    <p class="question">I would like to schedule an evaluation?</p>
    <div class="choice" style="left:20px"><i></i>yes</div>
    <div class="choice" style="left:77px"><i></i>not yet</div>
    <div class="submit">SUBMIT</div>
  </form>
  <p class="abs form-title">REQUEST INFORMATION</p>
</main>

<footer>
  <div class="abs footer-shade"></div>
  <p class="abs copyright">Copyright 2010 Moms Beyond Gnatflies! All Rights Reserved</p>
</footer>

</body>
</html>
```